Inspirational speaker and coach Corinne Valbeck is building a website

Design, Create and launch a 10-15 page Wordpress website. Please research Corinne online and use examples you have access to.

```html
<!DOCTYPE html>
<html lang="en">
<head>
<meta charset="utf-8">
<title>Corinne Valbeck — Inspirational Speaker and Coach</title>
<link rel="stylesheet" href="https://fonts.googleapis.com/css2?family=Lato:ital,wght@0,400;0,700;0,900;1,400;1,700&display=swap">
<style>
:root{
  --navy:#0e3a63;
  --orange:#f7931e;
  --grey-band:#ebebeb;
  --text:#3d3d3d;
  --ink:#161616;
  --white:#ffffff;
  --blue-deep:#0b3768;
  --blue-light:#1a86ad;
}
*{box-sizing:border-box;margin:0;padding:0}
html,body{width:1200px;height:3740px;overflow:hidden;background:var(--white)}
body{position:relative;font-family:"Lato",Arial,sans-serif;color:var(--text)}
.abs{position:absolute}
.shapes{position:absolute;left:0;top:0}

/* header / hero */
.brand{left:74px;top:52px;font-size:33px;font-weight:700;color:var(--white);letter-spacing:.5px}
.nav{top:62px;right:74px;display:flex;gap:44px;font-size:13px;font-weight:700;color:var(--white)}
.hero-title{left:72px;top:328px;font-size:64px;font-weight:700;color:var(--white);letter-spacing:1px}
.hero-tag{left:74px;top:403px;font-size:23px;font-style:italic;font-weight:700;color:var(--orange)}
.hero-text{left:74px;top:440px;width:560px;font-size:18.5px;line-height:32px;color:var(--white)}
.btn-outline{left:74px;top:523px;width:224px;height:48px;border:2px solid var(--orange);border-radius:24px;color:var(--white);font-size:15px;font-weight:700;display:flex;align-items:center;justify-content:center}

/* about */
.about-caption{left:95px;top:1416px;color:var(--white)}
.about-caption .name{font-size:26px;font-weight:700}
.about-caption .role{font-size:16px;margin-top:4px}
.section-title{font-size:29px;font-weight:900;color:var(--navy)}
.about-title{left:614px;top:1086px}
.about-text{left:615px;top:1135px;width:500px;font-size:16.5px;line-height:32.3px}
.btn-solid{background:var(--orange);color:var(--white);border-radius:24px;font-size:15px;font-weight:700;display:flex;align-items:center;justify-content:center}
.hire{left:614px;top:1444px;width:187px;height:45px}
.connect{display:flex;align-items:center;gap:14px;font-size:13px;font-weight:700;color:var(--navy)}
.connect .net{font-size:13px;font-weight:700;color:var(--ink)}
.about-connect{left:826px;top:1457px}

/* services */
.services-title{left:0;width:1200px;top:1680px;text-align:center}
.service{top:1762px;width:300px;text-align:center}
.service .icon{width:82px;height:82px;margin:0 auto;border-radius:50%;background:var(--navy);display:flex;align-items:center;justify-content:center}
.service h3{margin-top:22px;font-size:19px;font-weight:900;color:var(--orange)}
.service p{margin-top:10px;font-size:14.5px;line-height:24px}

/* testimonies */
.testi-title{left:0;width:1200px;top:2152px;text-align:center;font-size:29px;font-weight:900;color:var(--white)}
.testi-quote{left:250px;width:700px;top:2210px;text-align:center;font-size:18px;font-style:italic;line-height:29px;color:var(--white)}
.avatar{left:553px;top:2284px;width:94px;height:94px;border-radius:50%;border:3px solid var(--white);background:radial-gradient(circle at 50% 40%,#8a97a6,#2f3f55)}
.testi-name{left:0;width:1200px;top:2396px;text-align:center;font-size:14.5px;font-weight:900;color:var(--orange)}
.testi-loc{left:0;width:1200px;top:2418px;text-align:center;font-size:14px;font-style:italic;color:var(--white)}

/* news */
.news-title{left:74px;top:2622px}
.card{top:2677px;width:331px}
.card .thumb{height:200px}
.card .date{margin-top:18px;font-size:17px;font-weight:700;color:var(--orange)}
.card h4{margin-top:10px;font-size:19px;font-weight:900;color:var(--navy)}
.card p{margin-top:12px;font-size:14.5px;line-height:21px}

/* contact */
.contact-title{left:74px;top:3204px;font-size:29px;font-weight:700;color:var(--white)}
.contact-line{top:3280px;display:flex;align-items:center;gap:14px;color:var(--white);font-size:17px}
.ring{width:36px;height:36px;border-radius:50%;border:2px solid var(--white);display:flex;align-items:center;justify-content:center}
.field{background:var(--white);border-radius:18px;font-size:12px;color:var(--ink);padding:11px 20px}
.send{left:434px;top:3555px;width:166px;height:41px}

/* footer */
.copy{left:75px;top:3678px;font-size:14.5px;line-height:23px;color:var(--ink)}
.foot-connect{right:74px;top:3691px}
</style>
</head>
<body>

<!-- background shapes -->
<svg class="shapes" width="1200" height="3740" viewBox="0 0 1200 3740" aria-hidden="true">
  <defs>
    <linearGradient id="heroGrad" x1="0" y1="0" x2="1" y2="0">
      <stop offset="0" stop-color="#2d2f33"/>
      <stop offset=".45" stop-color="#4a4a46"/>
      <stop offset=".62" stop-color="#d8c78a"/>
      <stop offset=".78" stop-color="#c69a6e"/>
      <stop offset="1" stop-color="#5d5834"/>
    </linearGradient>
    <linearGradient id="testiGrad" x1="0" y1="0" x2="1" y2="1">
      <stop offset="0" stop-color="var(--blue-deep)"/>
      <stop offset=".5" stop-color="var(--blue-light)"/>
      <stop offset="1" stop-color="var(--blue-deep)"/>
    </linearGradient>
  </defs>
  <polygon points="0,0 1200,0 1200,912 0,760" fill="url(#heroGrad)"/>
  <polygon points="0,1046 1200,912 1200,1540 0,1668" fill="var(--grey-band)"/>
  <polygon points="0,2016 1200,2153 1200,2572 0,2435" fill="url(#testiGrad)"/>
  <polygon points="0,3121 1200,3251 1200,3654 0,3654" fill="var(--ink)"/>
</svg>

<!-- hero photo region -->
<div class="abs" role="img" aria-label="Portrait photograph of Corinne Valbeck with long blonde hair, wearing a leopard-print top" style="left:560px;top:0;width:640px;height:880px"></div>

<header>
  <div class="abs brand">CORINNE VALBECK</div>
  <nav class="abs nav"><span>ABOUT ME</span><span>SERVICES</span><span>NEWS &amp; EVENTS</span><span>TESTIMONIAL</span><span>BLOG</span><span>CONTACT</span></nav>
</header>

<section class="hero">
  <h1 class="abs hero-title">CORINNE VALBECK</h1>
  <div class="abs hero-tag">Inspirational speaker and coach</div>
  <p class="abs hero-text">Excepteur sint occaecat cupidatat non proident, sunt in culpa qui officia deserunt mollit anim id est laborum.</p>
  <div class="abs btn-outline">MORE ABOUT ME</div>
</section>

<section class="about">
  <svg class="abs" style="left:74px;top:924px" width="513" height="565" role="img" aria-label="Outdoor photograph of Corinne Valbeck in a black feathered outfit">
    <defs><linearGradient id="aboutGrad" x1="0" y1="0" x2="1" y2="1"><stop offset="0" stop-color="#6f8358"/><stop offset=".5" stop-color="#b9a48e"/><stop offset="1" stop-color="#2a2a2a"/></linearGradient></defs>
    <polygon points="0,0 513,58 513,565 0,565" fill="url(#aboutGrad)"/>
  </svg>
  <div class="abs about-caption"><div class="name">Corinne Valbeck</div><div class="role">Speaker and Coach</div></div>
  <h2 class="abs section-title about-title">ABOUT ME</h2>
  <p class="abs about-text">I am an experienced and seasoned business executive with expertise in operations, administration and management for multimillion-dollar companies. I possess a strong strategic vision with ability to pinpoint and resolve complex dynamic problems. I am particularly focused on organizational structure and believe in helping employees and executives realize their full potential. I have a proven track record of sustainably growing company revenue and business development.</p>
  <div class="abs btn-solid hire">HIRE ME</div>
  <div class="abs connect about-connect">CONNECT ME: <span class="net">Circlo</span><span class="net">Pixnest</span><span class="net">Workly</span></div>
</section>

<section class="services">
  <h2 class="abs section-title services-title">WHAT SERVICES OFFER</h2>
  <div class="abs service" style="left:90px">
    <div class="icon"><svg width="44" height="44" viewBox="0 0 44 44" fill="none" stroke="#fff" stroke-width="2"><circle cx="22" cy="10" r="6"/><path d="M12 28v-5a10 10 0 0 1 20 0v5"/><rect x="8" y="28" width="28" height="12"/></svg></div>
    <h3>NEMO ENIM</h3><p>Sed ut perspiciatis unde omnis iste natus error sit voluptatem accusantium doloremque beatae vitae.</p>
  </div>
  <div class="abs service" style="left:450px">
    <div class="icon"><svg width="44" height="44" viewBox="0 0 44 44" fill="none" stroke="#fff" stroke-width="2"><rect x="6" y="6" width="32" height="20"/><circle cx="12" cy="33" r="3"/><circle cx="22" cy="33" r="3"/><circle cx="32" cy="33" r="3"/><path d="M12 20l7-6 5 4 8-7"/></svg></div>
    <h3>NEMO ENIM</h3><p>Sed ut perspiciatis unde omnis iste natus error sit voluptatem accusantium doloremque beatae vitae.</p>
  </div>
  <div class="abs service" style="left:810px">
    <div class="icon"><svg width="44" height="44" viewBox="0 0 44 44" fill="none" stroke="#fff" stroke-width="2"><path d="M14 40v-8c-5-3-7-8-6-13a13 13 0 0 1 25 2l3 7h-4v5h-6v7"/><circle cx="22" cy="18" r="5"/><path d="M22 4v3M14 7l2 2M30 7l-2 2"/></svg></div>
    <h3>NEMO ENIM</h3><p>Sed ut perspiciatis unde omnis iste natus error sit voluptatem accusantium doloremque beatae vitae.</p>
  </div>
</section>

<section class="testimonies">
  <h2 class="abs testi-title">TESTIMONIES</h2>
  <p class="abs testi-quote">“ Sed vel magna vel eros adipiscing adipiscing eu sit amet turpismauris et massa sed lacus tempus pellentesque...”</p>
  <svg class="abs" style="left:509px;top:2320px" width="18" height="22" viewBox="0 0 18 22"><path d="M13 3L5 11l8 8" stroke="#fff" stroke-width="3" fill="none"/></svg>
  <svg class="abs" style="left:675px;top:2320px" width="18" height="22" viewBox="0 0 18 22"><path d="M5 3l8 8-8 8" stroke="#fff" stroke-width="3" fill="none"/></svg>
  <div class="abs avatar" role="img" aria-label="Client portrait photograph"></div>
  <div class="abs testi-name">NAME HEADING</div>
  <div class="abs testi-loc">Location</div>
</section>

<section class="news">
  <h2 class="abs section-title news-title">NEWS &amp; EVENTS</h2>
  <svg class="abs" style="left:1082px;top:2628px" width="44" height="24" viewBox="0 0 44 24"><path d="M12 4l-7 8 7 8M32 4l7 8-7 8" stroke="#333" stroke-width="3" fill="none"/></svg>
  <article class="abs card" style="left:74px">
    <div class="thumb" role="img" aria-label="Event promotion image with Corinne Valbeck for an inner circle membership" style="background:linear-gradient(90deg,#8a6a55,#4f5d45 45%,#5d6b52)"></div>
    <div class="date">AUG13, 2021</div><h4>LOREM IPSUM DOLOR SIT</h4>
    <p>Sed vel magna vel eros adipiscing adipiscing eu sit amet turpis. Mauris et massa sed lacus tempus pellentesque.</p>
  </article>
  <article class="abs card" style="left:434px">
    <div class="thumb" role="img" aria-label="Workshop promotion image with Corinne Valbeck about finding your inner warrior" style="background:linear-gradient(90deg,#8e9a76,#3a3a34 60%,#1a1850)"></div>
    <div class="date">AUG13, 2021</div><h4>LOREM IPSUM DOLOR SIT</h4>
    <p>Sed vel magna vel eros adipiscing adipiscing eu sit amet turpis. Mauris et massa sed lacus tempus pellentesque.</p>
  </article>
  <article class="abs card" style="left:793px">
    <div class="thumb" role="img" aria-label="Course promotion image with Corinne Valbeck about personal branding and marketing" style="background:linear-gradient(90deg,#9a9a94,#141414 35%,#0b0b0b)"></div>
    <div class="date">AUG13, 2021</div><h4>LOREM IPSUM DOLOR SIT</h4>
    <p>Sed vel magna vel eros adipiscing adipiscing eu sit amet turpis. Mauris et massa sed lacus tempus pellentesque.</p>
  </article>
</section>

<section class="contact">
  <svg class="abs" style="left:614px;top:3087px" width="512" height="567" role="img" aria-label="Winter outdoor photograph of Corinne Valbeck smiling">
    <defs><linearGradient id="contactGrad" x1="0" y1="0" x2="1" y2="1"><stop offset="0" stop-color="#8fb0d8"/><stop offset=".4" stop-color="#e6e1d8"/><stop offset="1" stop-color="#3a2a22"/></linearGradient></defs>
    <polygon points="0,58 512,0 512,567 0,567" fill="url(#contactGrad)"/>
  </svg>
  <h2 class="abs contact-title">CONTACT ME</h2>
  <div class="abs contact-line" style="left:74px">
    <span class="ring"><svg width="16" height="16" viewBox="0 0 16 16"><path d="M4 1l3 3-2 2c1 2 3 4 5 5l2-2 3 3-2 3C7 15 1 9 1 3z" fill="var(--orange)"/></svg></span>1-800-555-0148
  </div>
  <div class="abs contact-line" style="left:278px;font-size:14.5px">
    <span class="ring"><svg width="16" height="12" viewBox="0 0 16 12"><rect width="16" height="12" rx="1" fill="var(--orange)"/><path d="M0 1l8 6 8-6" stroke="var(--ink)" stroke-width="1.5" fill="none"/></svg></span>hello@valbeckcoaching.com
  </div>
  <div class="abs field" style="left:74px;top:3341px;width:256px;height:35px">Name</div>
  <div class="abs field" style="left:341px;top:3341px;width:256px;height:35px">Phone No.</div>
  <div class="abs field" style="left:74px;top:3391px;width:256px;height:35px">Email Address</div>
  <div class="abs field" style="left:341px;top:3391px;width:256px;height:35px">Subject</div>
  <div class="abs field" style="left:74px;top:3440px;width:524px;height:96px">Message</div>
  <div class="abs btn-solid send">SEND</div>
</section>

<footer>
  <p class="abs copy">Copyright © 2021. Valbeck Coaching.<br>All Right Reserved</p>
  <div class="abs connect foot-connect" style="color:var(--ink)">CONNECT ME: <span class="net">Circlo</span><span class="net">Pixnest</span><span class="net">Workly</span></div>
</footer>

</body>
</html>
```